Finance Product Agency Business Card Design

We're an agency that provides products (service contracts, gap insurance, tire and wheel, etc) and support to dealership finance departments. We specialize in training finance producers to maximize their potential and also keep them up to date on the ever changing compliance and legal landscape. I'll attach an image of our logo, excited to see what you all come up with. Would also be interested in discussing our new website design with the winner.

Target Market(s)

auto dealerships

Industry/Entity Type

Business

Contact Information for Business Card

Dale Hoskirk
Phone 517.364.2908
Fax 877.245.3196
email Dale.Hoskirk@brightlanecoverage.com

Requirements
Must have
• basic contact information
Nice to have
• looking for something professional but modern

```html
<!DOCTYPE html>
<html lang="en">
<head>
<meta charset="utf-8">
<title>Brightlane Coverage – Business Card</title>
<link href="https://fonts.googleapis.com/css2?family=Source+Sans+3:wght@400;700&display=swap" rel="stylesheet">
<style>
  :root {
    --slate: #3f5b6b;
    --slate-deep: #3b5868;
    --paper: #ffffff;
    --backdrop: #ece6dc;
    --shadow: rgba(40, 35, 25, 0.35);
  }
  html, body {
    margin: 0;
    padding: 0;
    width: 1189px;
    height: 1200px;
    overflow: hidden;
    background: var(--backdrop);
    font-family: "Source Sans 3", "Verdana", sans-serif;
  }
  .canvas {
    position: relative;
    width: 1189px;
    height: 1200px;
  }
  .card {
    position: absolute;
    left: 167px;
    width: 855px;
    height: 488px;
    box-shadow: 6px 8px 14px var(--shadow);
  }
  .card--front { top: 67px; background: var(--paper); }
  .card--back  { top: 627px; background: var(--slate-deep); }

  .brand {
    position: absolute;
    display: flex;
    align-items: center;
    gap: 22px;
  }
  .brand__mark {
    width: 96px;
    height: 96px;
    border-radius: 50%;
    flex: none;
  }
  .brand__name {
    font-weight: 700;
    font-size: 50px;
    line-height: 1;
    letter-spacing: 1px;
    text-transform: uppercase;
    white-space: nowrap;
  }
  .card--front .brand { left: 62px; top: 72px; }
  .card--front .brand__mark { background: var(--slate); }
  .card--front .brand__name { color: var(--slate); }

  .card--back .brand { left: 50%; top: 50%; transform: translate(-50%, -50%); }
  .card--back .brand__mark { background: var(--paper); }
  .card--back .brand__name { color: var(--paper); }

  .holder {
    position: absolute;
    right: 60px;
    top: 250px;
    margin: 0;
    font-weight: 700;
    font-size: 31px;
    letter-spacing: 0.5px;
    color: var(--slate);
    text-transform: uppercase;
  }
  .contact {
    position: absolute;
    left: 58px;
    top: 355px;
    margin: 0;
    padding: 0;
    list-style: none;
    color: var(--slate);
    font-size: 25px;
    line-height: 29px;
  }
  .contact__item {
    display: flex;
    align-items: center;
    gap: 14px;
  }
  .contact__icon {
    width: 22px;
    height: 22px;
    flex: none;
  }
</style>
</head>
<body>
<div class="canvas">

  <section class="card card--front" aria-label="Card front">
    <div class="brand">
      <span class="brand__mark"></span>
      <span class="brand__name">Brightlane Coverage</span>
    </div>

    <h1 class="holder">Dale Hoskirk</h1>

    <ul class="contact">
      <li class="contact__item">
        <svg class="contact__icon" viewBox="0 0 22 22" aria-label="Phone">
          <rect width="22" height="22" rx="3" fill="#3f5b6b"/>
          <path d="M5 9c0-3 12-3 12 0v1h-3V8.5H8V10H5z" fill="#fff"/>
          <rect x="6" y="11" width="10" height="6" rx="1" fill="#fff"/>
          <circle cx="11" cy="14" r="1.6" fill="#3f5b6b"/>
        </svg>
        <span>517.364.2908</span>
      </li>
      <li class="contact__item">
        <svg class="contact__icon" viewBox="0 0 22 22" aria-label="Fax">
          <rect width="22" height="22" rx="3" fill="#3f5b6b"/>
          <rect x="7" y="4" width="8" height="5" fill="#fff"/>
          <rect x="4" y="9" width="14" height="6" rx="1" fill="#fff"/>
          <rect x="7" y="13" width="8" height="5" fill="#fff" stroke="#3f5b6b" stroke-width="1"/>
        </svg>
        <span>877.245.3196</span>
      </li>
      <li class="contact__item">
        <svg class="contact__icon" viewBox="0 0 22 22" aria-label="Email">
          <rect width="22" height="22" rx="3" fill="#3f5b6b"/>
          <rect x="4" y="6" width="14" height="10" fill="none" stroke="#fff" stroke-width="1.5"/>
          <path d="M4 6l7 6 7-6M4 16l5-5M18 16l-5-5" fill="none" stroke="#fff" stroke-width="1.3"/>
        </svg>
        <span>Dale.Hoskirk@brightlanecoverage.com</span>
      </li>
    </ul>
  </section>

  <section class="card card--back" aria-label="Card back">
    <div class="brand">
      <span class="brand__mark"></span>
      <span class="brand__name">Brightlane Coverage</span>
    </div>
  </section>

</div>
</body>
</html>
```